Project Manager Business Card for Top Architectural Firm

Update and design a stunning Senior Project Manager Business Card

MARCO T. RUEDA II
Senior Project Manager

H A R B O R L I N E
A R C H I T E C T U R E L L C.
www.HarborlineCrestHouses.com
4217 NW 38th Ter. Suite 905
Miami, FL 33172
C: (305) 418-2273
mrueda.harborlinecresthouses@mailvista.net

Looking to have the logo to be UV Spot ink printed and to be prominent.

Target Market(s)

High end real estate architecture construction

Industry/Entity Type

Architect

Contact Information for Business Card

MARCO T. RUEDA II
Senior Project Manager

H A R B O R L I N E
Miami, FL 33172
C: (305) 418-2273

Font styles to use
Sans Serif

Colors

Designer to choose colors to be used in the design.

Requirements
Must have
• Prominent Logo

```html
<!DOCTYPE html>
<html lang="en">
<head>
<meta charset="utf-8">
<title>Harborline Architecture – Business Card</title>
<link href="https://fonts.googleapis.com/css2?family=Montserrat:wght@300;500;800&display=swap" rel="stylesheet">
<style>
  :root {
    --page: #1b1b1d;
    --card: #2a2a2c;
    --card-edge: #1f1f21;
    --uv-gloss: #3a3a3d;
    --accent: #2f97d9;
    --ink: #f2f2f2;
    --muted: #d8d8d8;
  }
  * { box-sizing: border-box; margin: 0; padding: 0; }
  html, body { width: 1200px; height: 914px; overflow: hidden; }
  body {
    background: var(--page);
    font-family: "Montserrat", Arial, sans-serif;
    position: relative;
  }
  .card {
    position: absolute;
    left: 250px;
    width: 700px;
    height: 400px;
    background: var(--card);
    border-bottom: 3px solid var(--card-edge);
    box-shadow: 0 10px 30px rgba(0,0,0,.5);
  }
  .card--back { top: 37px; }
  .card--front { top: 477px; }

  /* Back: UV spot wordmark */
  .back-mark {
    position: absolute;
    inset: 0;
    display: flex;
    flex-direction: column;
    align-items: center;
    justify-content: center;
    gap: 14px;
  }
  .back-mark__dot {
    width: 70px; height: 70px; border-radius: 50%;
    background: var(--uv-gloss);
  }
  .back-mark__name,
  .back-mark__sub {
    color: var(--uv-gloss);
    font-weight: 300;
    text-align: center;
  }
  .back-mark__name { font-size: 44px; letter-spacing: 8px; }
  .back-mark__sub { font-size: 13px; letter-spacing: 5px; }

  /* Front */
  .brand {
    position: absolute;
    left: 30px; top: 80px;
    width: 270px;
    display: flex;
    flex-direction: column;
    align-items: center;
    gap: 14px;
  }
  .brand__dot {
    width: 78px; height: 78px; border-radius: 50%;
    background: var(--accent);
  }
  .brand__name,
  .brand__sub {
    color: var(--ink);
    font-weight: 300;
    text-align: center;
  }
  .brand__name { font-size: 32px; letter-spacing: 5px; }
  .brand__sub { font-size: 11px; letter-spacing: 3.5px; margin-top: -6px; }

  .divider {
    position: absolute;
    left: 312px; top: 56px;
    width: 2px; height: 270px;
    background: var(--accent);
  }
  .details {
    position: absolute;
    left: 334px; top: 58px;
    width: 356px;
    color: var(--ink);
  }
  .details__name {
    color: var(--accent);
    font-weight: 800;
    font-size: 27px;
    letter-spacing: .5px;
  }
  .details__title {
    font-size: 12px;
    font-weight: 500;
    letter-spacing: 3.4px;
    text-transform: uppercase;
    margin-top: 4px;
  }
  .contact { list-style: none; margin-top: 28px; }
  .contact__item {
    display: flex;
    align-items: flex-start;
    gap: 10px;
    font-size: 13px;
    line-height: 1.5;
    color: var(--muted);
    margin-bottom: 6px;
  }
  .contact__item--gap { margin-top: 24px; }
  .contact__icon { width: 14px; height: 14px; flex: none; margin-top: 3px; fill: var(--accent); }
  .contact__email { font-size: 11.5px; }
</style>
</head>
<body>

<section class="card card--back" aria-label="Card back">
  <div class="back-mark">
    <span class="back-mark__dot"></span>
    <div class="back-mark__name">HARBORLINE</div>
    <div class="back-mark__sub">ARCHITECTURE LLC.</div>
  </div>
</section>

<section class="card card--front" aria-label="Card front">
  <div class="brand">
    <span class="brand__dot"></span>
    <div class="brand__name">HARBORLINE</div>
    <div class="brand__sub">ARCHITECTURE LLC.</div>
  </div>

  <div class="divider"></div>

  <div class="details">
    <h1 class="details__name">MARCO T. RUEDA II</h1>
    <p class="details__title">Senior Project Manager</p>

    <ul class="contact">
      <li class="contact__item">
        <svg class="contact__icon" viewBox="0 0 24 24"><path d="M12 2a7 7 0 0 0-7 7c0 5 7 13 7 13s7-8 7-13a7 7 0 0 0-7-7zm0 9.5A2.5 2.5 0 1 1 12 6.5a2.5 2.5 0 0 1 0 5z"/></svg>
        <span>4217 NW 38th Ter. Suite 905<br>Miami, FL 33172</span>
      </li>
      <li class="contact__item contact__item--gap">
        <svg class="contact__icon" viewBox="0 0 24 24"><path d="M6.6 10.8a15.1 15.1 0 0 0 6.6 6.6l2.2-2.2a1 1 0 0 1 1-.25 11.4 11.4 0 0 0 3.6.57 1 1 0 0 1 1 1V20a1 1 0 0 1-1 1A17 17 0 0 1 3 4a1 1 0 0 1 1-1h3.5a1 1 0 0 1 1 1c0 1.25.2 2.45.57 3.57a1 1 0 0 1-.25 1z"/></svg>
        <span>(305) 418-2273</span>
      </li>
      <li class="contact__item">
        <svg class="contact__icon" viewBox="0 0 24 24"><path d="M2 5h20v14H2zm2 2v.5l8 5 8-5V7l-8 5z"/></svg>
        <span class="contact__email">mrueda.harborlinecresthouses@mailvista.net</span>
      </li>
      <li class="contact__item">
        <svg class="contact__icon" viewBox="0 0 24 24"><path d="M12 2a10 10 0 1 0 0 20 10 10 0 0 0 0-20zm7.9 9h-3.4a15 15 0 0 0-1.3-5.8A8 8 0 0 1 19.9 11zM12 4c.9 1.2 2.2 3.6 2.5 7h-5C9.8 7.6 11.1 5.2 12 4zM8.8 5.2A15 15 0 0 0 7.5 11H4.1a8 8 0 0 1 4.7-5.8zM4.1 13h3.4a15 15 0 0 0 1.3 5.8A8 8 0 0 1 4.1 13zm7.9 7c-.9-1.2-2.2-3.6-2.5-7h5c-.3 3.4-1.6 5.8-2.5 7zm3.2-1.2a15 15 0 0 0 1.3-5.8h3.4a8 8 0 0 1-4.7 5.8z"/></svg>
        <span>www.HarborlineCrestHouses.com</span>
      </li>
    </ul>
  </div>
</section>

</body>
</html>
```